Steady Harvest of Patrons Programme Graphic

Please refer to attached graphic.
I wish to redesign this graphic to represent a programme of work that we (Brinvo) deliver to our customers.
The design represents 9 steps ( 3 steps at each of 3 levels) and is all about implementing the 'Steady Harvest of Patrons'

I like the fact that the increasing business growth is evident when you are progressing through the stages, but the current graphic looks dated and the colours are not working.
I would also like to incorporate the SHP logo we have created.

Target Market(s)

IT Sector - businesses looking to grow

Industry/Entity Type

We are a digital marketing company

Requirements
Must have
• Clear, concise design
Should not have
• Design must not be complicated

```html
<!DOCTYPE html>
<html lang="en">
<head>
<meta charset="utf-8">
<title>Steady Harvest of Patrons – Programme Graphic</title>
<link rel="stylesheet" href="https://fonts.googleapis.com/css2?family=Montserrat:wght@500;600;700;800&family=Open+Sans:wght@400;500&display=swap">
<style>
  :root {
    --blue-deep: #0b69ae;
    --blue-mid: #1389cf;
    --blue-light: #22b2ea;
    --green-deep: #137f3a;
    --green-mid: #3aa53c;
    --green-light: #9ccb3b;
    --red-deep: #8e0b0e;
    --red-mid: #c9161d;
    --red-light: #f07a5c;
    --title-red: #e8553f;
    --title-green: #1d8a43;
    --rule-orange: #f5a623;
    --logo-blue: #1e9ad6;
    --ink: #111111;
    --white: #ffffff;
  }
  html, body {
    margin: 0;
    padding: 0;
    width: 1200px;
    height: 1200px;
    overflow: hidden;
    background: var(--white);
  }
  .canvas { display: block; width: 1200px; height: 1200px; }
  .title { font-family: "Open Sans", sans-serif; font-size: 44px; font-weight: 400; }
  .title-business { fill: var(--title-red); }
  .title-value { fill: var(--title-green); }
  .roof-label { font-family: "Montserrat", sans-serif; font-size: 17px; font-weight: 700; fill: var(--ink); }
  .step-number { font-family: "Montserrat", sans-serif; font-size: 40px; font-weight: 800; fill: var(--ink); text-anchor: middle; }
  .step-box { fill: var(--blue-deep); }
  .step-items { font-family: "Montserrat", sans-serif; font-size: 11.5px; font-weight: 500; fill: var(--white); text-anchor: middle; }
  .band-heading { font-family: "Montserrat", sans-serif; font-size: 15px; font-weight: 700; fill: var(--white); text-anchor: middle; }
  .band-sub { font-family: "Open Sans", sans-serif; font-size: 14px; font-weight: 500; fill: var(--white); text-anchor: middle; }
  .brand-mark { font-family: "Montserrat", sans-serif; font-weight: 800; fill: var(--logo-blue); }
  .brand-square { fill: none; stroke: var(--logo-blue); stroke-width: 8; }
  .agency-name { font-family: "Montserrat", sans-serif; font-weight: 800; font-size: 48px; fill: var(--logo-blue); }
</style>
</head>
<body>
<svg class="canvas" viewBox="0 0 1000 1000" xmlns="http://www.w3.org/2000/svg" aria-label="Steady Harvest of Patrons programme: three rising stages of business value">
  <defs>
    <linearGradient id="blueLeft" x1="0" y1="1" x2="1" y2="0">
      <stop offset="0" stop-color="var(--blue-deep)"/><stop offset="1" stop-color="var(--blue-mid)"/>
    </linearGradient>
    <linearGradient id="blueRight" x1="0" y1="0" x2="1" y2="1">
      <stop offset="0" stop-color="var(--blue-light)"/><stop offset="1" stop-color="#0fa0df"/>
    </linearGradient>
    <linearGradient id="greenLeft" x1="0" y1="1" x2="1" y2="0">
      <stop offset="0" stop-color="var(--green-deep)"/><stop offset="1" stop-color="var(--green-mid)"/>
    </linearGradient>
    <linearGradient id="greenRight" x1="0" y1="0" x2="1" y2="1">
      <stop offset="0" stop-color="#6dbb3a"/><stop offset="1" stop-color="var(--green-light)"/>
    </linearGradient>
    <linearGradient id="redLeft" x1="0" y1="1" x2="1" y2="0">
      <stop offset="0" stop-color="var(--red-deep)"/><stop offset="1" stop-color="var(--red-mid)"/>
    </linearGradient>
    <linearGradient id="redRight" x1="0" y1="0" x2="0" y2="1">
      <stop offset="0" stop-color="var(--red-light)"/><stop offset="1" stop-color="#ec5a45"/>
    </linearGradient>
    <linearGradient id="bandFill" x1="0" y1="0" x2="1" y2="0">
      <stop offset="0" stop-color="#dc1f26"/><stop offset="1" stop-color="#6e0608"/>
    </linearGradient>
  </defs>

  <!-- Heading -->
  <text class="title" x="152" y="257"><tspan class="title-business">Business</tspan> <tspan class="title-value">Value</tspan></text>
  <g class="title-rules" stroke-width="2.5">
    <line x1="140" y1="270" x2="245" y2="270" stroke="var(--blue-mid)"/>
    <line x1="250" y1="270" x2="355" y2="270" stroke="var(--title-green)"/>
    <line x1="360" y1="270" x2="465" y2="270" stroke="var(--rule-orange)"/>
  </g>

  <!-- Growth arrow -->
  <path class="growth-arrow" fill="var(--blue-deep)" d="M175 748 V343 H142 L192.5 292 L243 343 H210 V748 Z"/>

  <!-- Stage 3 -->
  <g class="stage stage-three">
    <path fill="url(#redLeft)" d="M583 590 V350 L720 263 V590 Z"/>
    <path fill="url(#redRight)" d="M720 263 L800 318 V590 H720 Z"/>
  </g>
  <!-- Stage 2 -->
  <g class="stage stage-two">
    <path fill="url(#greenLeft)" d="M413 590 V440 L550 356 V590 Z"/>
    <path fill="url(#greenRight)" d="M550 356 L630 408 V590 H550 Z"/>
  </g>
  <!-- Stage 1 -->
  <g class="stage stage-one">
    <path fill="url(#blueLeft)" d="M248 590 V540 L385 450 V590 Z"/>
    <path fill="url(#blueRight)" d="M385 450 L465 505 V590 H385 Z"/>
  </g>

  <!-- Roof labels -->
  <text class="roof-label" transform="translate(268 513) rotate(-33)">Steady</text>
  <text class="roof-label" transform="translate(428 423) rotate(-32)">Harvest</text>
  <text class="roof-label" transform="translate(597 332) rotate(-32)">Patrons</text>

  <!-- Step badges -->
  <g class="step-badge">
    <circle cx="383" cy="571" r="45" fill="var(--blue-deep)"/>
    <circle cx="383" cy="566" r="41" fill="var(--white)"/>
    <text class="step-number" x="383" y="580">1</text>
  </g>
  <g class="step-badge">
    <circle cx="548" cy="571" r="45" fill="var(--green-mid)"/>
    <circle cx="548" cy="566" r="41" fill="var(--white)"/>
    <text class="step-number" x="548" y="580">2</text>
  </g>
  <g class="step-badge">
    <circle cx="718" cy="571" r="45" fill="var(--red-deep)"/>
    <circle cx="718" cy="566" r="41" fill="var(--white)"/>
    <text class="step-number" x="718" y="580">3</text>
  </g>

  <!-- Step boxes -->
  <g class="step-list">
    <rect class="step-box" x="318" y="622" width="127" height="56" rx="10"/>
    <text class="step-items" x="381.5" y="637"><tspan x="381.5">Personas</tspan><tspan x="381.5" dy="14">Database</tspan><tspan x="381.5" dy="14">Systems</tspan></text>
  </g>
  <g class="step-list">
    <rect class="step-box" x="488" y="622" width="127" height="56" rx="10"/>
    <text class="step-items" x="551.5" y="637"><tspan x="551.5">Messaging</tspan><tspan x="551.5" dy="14">Leads</tspan><tspan x="551.5" dy="14">Pipeline</tspan></text>
  </g>
  <g class="step-list">
    <rect class="step-box" x="658" y="622" width="127" height="56" rx="10"/>
    <text class="step-items" x="721.5" y="637"><tspan x="721.5">Sales</tspan><tspan x="721.5" dy="14">Nurture</tspan><tspan x="721.5" dy="14">Reference</tspan></text>
  </g>

  <!-- Review band -->
  <rect class="review-band" x="248" y="688" width="552" height="58" rx="6" fill="url(#bandFill)"/>
  <text class="band-heading" x="345" y="710">Numbers that Matter</text>
  <text class="band-sub" x="345" y="728">Foundation Metrics</text>
  <text class="band-heading" x="529" y="710">Weekly Scorecard</text>
  <text class="band-sub" x="529" y="728">Tactical Execution</text>
  <text class="band-heading" x="707" y="710">Numbers that Matter</text>
  <text class="band-sub" x="707" y="728">Strategic Review</text>

  <!-- Programme mark -->
  <g class="programme-mark">
    <rect class="brand-square" x="712" y="92" width="50" height="50"/>
    <text class="brand-mark" x="712" y="200" font-size="56">SHP</text>
  </g>

  <!-- Agency name -->
  <text class="agency-name" x="660" y="862">Brinvo</text>
</svg>
</body>
</html>
```